Coffeeshop menu for filter tip

We want to have a cannabis (coffeeshop) menu in the size 25mm wide x 60mm wide. Some examples attached.

it must have the following text:
Menu

WEED p/g
Velotrine €16
Cinderfox €14
Tide Rambler €14
Marigolden €16
Grand Pelican €14
Copper Comet €14

HASH p/g
Baltic Ember €12
Harbor Velvet€11
Plum Rova €14
Dusk Maple €10

Target Market(s)

tourist in Canal Leaf

Requirements
Nice to have
• cannabis sign leaf
• No Cigarettes allowed symbol

```html
<!DOCTYPE html>
<html lang="en">
<head>
<meta charset="utf-8">
<title>Canal Leaf Coffeeshop Menu</title>
<link href="https://fonts.googleapis.com/css2?family=Montserrat:wght@400;500;700&family=Tinos&display=swap" rel="stylesheet">
<style>
  :root {
    --page: #ecebe8;
    --card: #2b2c2b;
    --card-deep: #1f2220;
    --line: #f2f2f2;
    --title: #e6ee12;
    --accent: #ff1f1f;
    --text: #ffffff;
  }
  * { margin: 0; padding: 0; box-sizing: border-box; }
  html, body { width: 1200px; height: 1200px; overflow: hidden; background: var(--page); }
  .menu-card {
    position: absolute; left: 367px; top: 40px; width: 466px; height: 1120px;
    background: linear-gradient(180deg, var(--card) 0%, var(--card) 45%, var(--card-deep) 100%);
    color: var(--text); font-family: "Montserrat", sans-serif;
    box-shadow: 0 10px 30px rgba(0,0,0,.25);
  }
  .leaf-backdrop {
    position: absolute; left: 30px; top: 560px; width: 410px; height: 520px;
    background: radial-gradient(ellipse at 55% 45%, rgba(60,95,55,.55) 0%, rgba(47,69,48,.25) 45%, rgba(0,0,0,0) 72%);
  }
  .card-frame { position: absolute; inset: 0; }
  .shop-name {
    position: absolute; top: 108px; left: 0; width: 100%; text-align: center;
    font-weight: 700; font-size: 50px; line-height: 1; color: var(--title);
  }
  .menu-band {
    position: absolute; left: 128px; top: 171px; width: 210px; height: 29px;
    background: var(--accent); display: flex; align-items: center; justify-content: center;
    font-weight: 700; font-size: 24px; letter-spacing: 18px; padding-left: 18px; color: var(--text);
  }
  .section-head {
    position: absolute; font-family: "Tinos", serif; font-size: 29px; color: var(--text);
    padding: 0 6px 4px; border-bottom: 2px dashed var(--accent);
  }
  .price-list { position: absolute; left: 46px; width: 320px; list-style: none; }
  .price-list li { position: relative; height: 40px; font-size: 28px; line-height: 40px; white-space: nowrap; }
  .price-list .price { position: absolute; left: 268px; color: var(--accent); font-weight: 500; }
  .hash-list li { height: 41px; line-height: 41px; }
  .section-divider { position: absolute; left: 48px; width: 349px; top: 623px; border-top: 2px dashed var(--line); }
  .no-smoking {
    position: absolute; top: 975px; left: 0; width: 100%; display: flex; justify-content: center;
    align-items: center; gap: 12px; font-size: 28px;
  }
</style>
</head>
<body>
<div class="menu-card">
  <div class="leaf-backdrop" role="img" aria-label="Faint cannabis leaf illustration in the background"></div>

  <svg class="card-frame" width="466" height="1120" viewBox="0 0 466 1120">
    <path d="M60 22 H406 Q414 60 448 64 V1056 Q414 1060 406 1098 H60 Q52 1060 18 1056 V64 Q52 60 60 22 Z"
          fill="none" stroke="#f2f2f2" stroke-width="2.5"/>
    <rect x="24" y="34" width="418" height="1052" fill="none" stroke="#f2f2f2" stroke-width="1.5" stroke-dasharray="8 6"/>
  </svg>

  <h1 class="shop-name">Canal Leaf</h1>
  <div class="menu-band">MENU</div>

  <div class="section-head" style="left:50px; top:264px;">WEED</div>
  <div class="section-head" style="left:258px; top:264px;">PRICE P/G</div>
  <ul class="price-list" style="top:335px;">
    <li>Velotrine<span class="price">€16</span></li>
    <li>Cinderfox<span class="price">€14</span></li>
    <li>Tide Rambler<span class="price">€14</span></li>
    <li>Marigolden<span class="price">€16</span></li>
    <li>Grand Pelican<span class="price">€14</span></li>
    <li>Copper Comet<span class="price">€14</span></li>
  </ul>

  <div class="section-divider"></div>

  <div class="section-head" style="left:50px; top:679px;">HASH</div>
  <div class="section-head" style="left:258px; top:679px;">PRICE P/G</div>
  <ul class="price-list hash-list" style="top:738px; left:52px;">
    <li>Baltic Ember<span class="price" style="left:260px;">€12</span></li>
    <li>Harbor Velvet<span class="price" style="left:260px;">€11</span></li>
    <li>Plum Rova<span class="price" style="left:260px;">€14</span></li>
    <li>Dusk Maple<span class="price" style="left:260px;">€10</span></li>
  </ul>

  <div class="no-smoking">
    <svg width="40" height="40" viewBox="0 0 40 40" aria-hidden="true">
      <circle cx="20" cy="20" r="17" fill="#ffffff" stroke="#ff2b2b" stroke-width="3.5"/>
      <rect x="9" y="18" width="20" height="5" fill="#444"/>
      <rect x="26" y="18" width="4" height="5" fill="#ff2b2b"/>
      <line x1="8" y1="8" x2="32" y2="32" stroke="#ff2b2b" stroke-width="3.5"/>
    </svg>
    <span>No sigarates</span>
  </div>
</div>
</body>
</html>
```